Veranstaltungsservice für Firmenfeste sucht Logo & Visitenkarte
Zielgruppe
Zielgruppe: Firmen
Wir sind ein veranstaltungsservice für Firmenfeste. Wir haben das Equipment von A bis Z. Hierbei geht es nicht rein nur, um das Equipment von einem Event sondern auch um aktivitäten ( ab 3 Jahre bis 99Jahre). Wir liefern, bauen auf, moderrieren durchs Programm und orgranisieren Abbau und den Rücktransport. Es wäre sinnvoll wenn Sie sich unseren Image Film anschauen, da erfahren Sie sehr viel über uns.
Wir möchten nochmal deutlich drauf hinweissen, dass es in Zukunft mehr in richtung Erwachsene gehen soll, anstatt Kinder. Allerdings werden wir den Nachwuchs nicht vernachlässigen.
Link für HP und Image film: https://www.festhalmwiese.example/home/
Aufgabenstellung
- Gerne in einer Form wie z.B in einem Kreis oder ähnlichem. Die gefielen uns auch in den Vorschlägen gut
- Soll nicht verspielt aussehen
- Wir wollen in Zukunft vorallem Erwachsene ansprechen und Aktivitäten mit ihnen durchführen. Wobei wir den Nachwuchs nicht vernachlässigen werden!
- Gerne eine Kreative aber gut Lesbare Schriftart
- Da blau unser Firmenfarbe ist, sollte es berücksichtigt werden.
- Wir haben die Rot tönne mit ausgewählt, da diese für aktivität stehen
- Wenn man unser Ziel reinbringen könnte wäre es wünschenswert: Mitarbeiter sollen lange von dem Fest reden. Dadurch soll eine Motivation des Teams entstehen, wovon die Arbeitgeben provitieren.
- Gerne auch Bilder von Hauptatraktionen wie das beleuchtete zelt. ( Kein Muss!!!!!)
Wir hoffen auf Ihre Ideen und Vorschläge.

```html
<!DOCTYPE html>
<html lang="de">
<head>
<meta charset="utf-8">
<title>Festhalm Event – Visitenkarte</title>
<link rel="stylesheet" href="https://fonts.googleapis.com/css2?family=Arimo:wght@400;700&display=swap">
<style>
  :root {
    --brand-blue: #0097db;
    --band-dark: #383838;
    --band-mid: #444444;
    --text-light: #ffffff;
    --shadow: rgba(0, 0, 0, 0.45);
  }
  html, body {
    margin: 0;
    padding: 0;
    overflow: hidden;
    background: #ffffff;
  }
  .business-card {
    position: relative;
    width: 1200px;
    height: 686px;
    overflow: hidden;
    background: var(--brand-blue);
    font-family: "Arimo", Arial, sans-serif;
    color: var(--text-light);
  }
  .card-bands {
    position: absolute;
    inset: 0;
  }
  .brand-block {
    position: absolute;
    left: 79px;
    top: 300px;
    width: 300px;
    text-align: center;
  }
  .brand-ring {
    display: block;
    margin: 0 auto 26px;
  }
  .brand-name {
    font-weight: 700;
    font-size: 28px;
    letter-spacing: 0.3px;
    margin: 0;
  }
  .brand-since {
    font-size: 20px;
    margin: 10px 0 0;
  }
  .contact-icon {
    position: absolute;
  }
  .contact-text {
    position: absolute;
    margin: 0;
    font-size: 25px;
    line-height: 34px;
    white-space: nowrap;
  }
  .contact-address { left: 618px; top: 128px; }
  .contact-phone   { left: 680px; top: 260px; }
  .contact-mail    { left: 760px; top: 392px; }
  .contact-web     { left: 839px; top: 528px; }
</style>
</head>
<body>
<div class="business-card">
  <svg class="card-bands" width="1200" height="686" viewBox="0 0 1200 686" aria-hidden="true">
    <defs>
      <filter id="band-shadow" x="-20%" y="-20%" width="140%" height="140%">
        <feDropShadow dx="-6" dy="0" stdDeviation="9" flood-color="#000" flood-opacity="0.45"/>
      </filter>
      <linearGradient id="inner-shade" x1="0" y1="0" x2="1" y2="0.2">
        <stop offset="0" stop-color="#2e2e2e"/>
        <stop offset="0.12" stop-color="#424242"/>
        <stop offset="1" stop-color="#464646"/>
      </linearGradient>
    </defs>
    <polygon class="band-outer" points="314,0 958,0 1200,395 1200,686 703,686" fill="var(--band-dark)" filter="url(#band-shadow)"/>
    <polygon class="band-inner" points="440,0 958,0 1200,395 1200,686 846,686" fill="url(#inner-shade)" filter="url(#band-shadow)"/>
  </svg>

  <div class="brand-block">
    <svg class="brand-ring" width="150" height="150" viewBox="0 0 150 150" aria-hidden="true">
      <circle cx="75" cy="75" r="68" fill="none" stroke="var(--text-light)" stroke-width="8"/>
    </svg>
    <p class="brand-name">Festhalm Event</p>
    <p class="brand-since">seit 1985</p>
  </div>

  <svg class="contact-icon icon-pin" style="left:446px;top:140px" width="42" height="56" viewBox="0 0 42 56" aria-hidden="true">
    <path d="M21 0C9.4 0 0 9.4 0 21c0 14 21 35 21 35s21-21 21-35C42 9.4 32.6 0 21 0zm0 29a8 8 0 1 1 0-16 8 8 0 0 1 0 16z" fill="var(--text-light)"/>
  </svg>

  <svg class="contact-icon icon-phone" style="left:512px;top:262px" width="56" height="42" viewBox="0 0 56 42" aria-hidden="true">
    <path d="M4 12C4 4 14 1 28 1s24 3 24 11v4h-11v-5c-4-1-8-1.5-13-1.5S19 10 15 11v5H4z" fill="var(--text-light)"/>
    <path d="M17 14h22l8 14v13H9V28z" fill="var(--text-light)"/>
    <circle cx="28" cy="28" r="7" fill="var(--band-mid)"/>
    <circle cx="28" cy="28" r="3" fill="var(--text-light)"/>
  </svg>

  <svg class="contact-icon icon-mail" style="left:587px;top:407px" width="56" height="34" viewBox="0 0 56 34" aria-hidden="true">
    <rect x="0" y="0" width="56" height="34" fill="var(--text-light)"/>
    <path d="M1 1l27 19L55 1M1 33l20-16M55 33L35 17" fill="none" stroke="var(--band-dark)" stroke-width="2"/>
  </svg>

  <svg class="contact-icon icon-globe" style="left:662px;top:532px" width="54" height="54" viewBox="0 0 54 54" aria-hidden="true">
    <g fill="none" stroke="var(--text-light)" stroke-width="2.6">
      <circle cx="27" cy="27" r="24"/>
      <ellipse cx="27" cy="27" rx="11" ry="24"/>
      <line x1="27" y1="3" x2="27" y2="51"/>
      <line x1="3" y1="27" x2="51" y2="27"/>
      <path d="M7 15h40M7 39h40"/>
    </g>
  </svg>

  <p class="contact-text contact-address">Am Lindenanger 7<br>53999 Wiesental - Oberhalm</p>
  <p class="contact-text contact-phone">04321 - 587</p>
  <p class="contact-text contact-mail">info@festhalmwiese.example</p>
  <p class="contact-text contact-web">festhalmwiese.example</p>
</div>
</body>
</html>
```